fernbolt website

commerce website to sell cookeries, brackets, mailboxes and to show off homes built. Modern Steel in design see kelvo rides web page to be like: https://www.kelvorides.com/en/ sorry its blue mantis hosting word press divi

must be able to add products to page

Target Market(s)

mainly western states of U.S.

Industry/Entity Type

Building Product

Coding

Coded - Design and coding required

Number of Pages Required

3 page

Font styles to use
Sans Serif

Colors

Designer to choose colors to be used in the design.

Requirements
Must have
• customers to be able to order products from page
• blue mantis hosting word press divi

```html
<!DOCTYPE html>
<html lang="en">
<head>
<meta charset="utf-8">
<title>Fernbolt — Contact Us</title>
<link href="https://fonts.googleapis.com/css2?family=Poppins:wght@400;500;600&family=Roboto:wght@400;500&display=swap" rel="stylesheet">
<style>
:root{
  --brand:#3f5e8c;
  --brand-dark:#3b5987;
  --page:#f5f5f6;
  --white:#ffffff;
  --ink:#222a33;
  --muted:#555b63;
  --field-text:#6b7077;
  --map:#e4e2dc;
  --rule:rgba(255,255,255,.22);
}
*{margin:0;padding:0;box-sizing:border-box}
html,body{width:870px;height:1200px;overflow:hidden}
body{position:relative;background:var(--page);font-family:'Poppins',sans-serif;color:var(--ink)}
.abs{position:absolute}

/* header */
.site-header{left:0;top:0;width:870px;height:88px;background:var(--brand);color:var(--white);font-family:'Roboto',sans-serif}
.brand{left:63px;top:24px;display:flex;align-items:center;gap:7px;font-family:'Poppins',sans-serif;font-weight:500;font-size:19px;letter-spacing:1px;color:var(--white)}
.brand-mark{width:14px;height:14px;background:var(--white)}
.main-nav{left:241px;top:15px;display:flex;gap:19px;font-size:9.8px}
.top-links{right:65px;top:17px;font-size:8.8px}
.search{left:243px;top:42px;width:312px;height:27px;background:var(--white);border-radius:2px;display:flex;align-items:center;font-size:7.8px;color:#666}
.search .cat{width:32px;text-align:center;border-right:1px solid #ddd;height:100%;line-height:27px;font-weight:500;color:#444}
.search .ph{padding-left:14px;flex:1}
.search .go{width:35px;height:27px;background:#5c7fb0;display:flex;align-items:center;justify-content:center}
.acct{top:45px;display:flex;align-items:center;gap:5px;font-size:8.6px;line-height:1.2;color:#dfe6f0}
.acct b{font-weight:400;color:var(--white);font-size:9.4px}

/* title bar */
.title-bar{left:0;top:88px;width:870px;height:45px;background:var(--white)}
.title-bar h1{position:absolute;left:64px;top:14px;font-size:12.6px;font-weight:500;letter-spacing:.4px}
.crumbs{position:absolute;right:65px;top:15px;font-size:10.4px;color:var(--ink)}

/* content */
.section-title{font-size:23px;font-weight:500;letter-spacing:.3px;line-height:1;top:200px}
.lead{font-size:11px;line-height:18px;color:var(--muted);top:232px;width:370px}
.field{background:var(--white);border-radius:3px;font-size:10.3px;color:var(--field-text);padding:9px 11px}
.send{left:64px;top:459px;width:76px;height:29px;background:var(--brand-dark);color:var(--white);border-radius:3px;font-size:10.5px;font-weight:500;text-align:center;line-height:29px}
.info-h{left:459px;font-size:13.5px;font-weight:600}
.info-t{left:460px;font-size:11px;line-height:18px;color:var(--muted)}
.map{left:64px;top:538px;width:741px;height:316px;background:linear-gradient(135deg,#e8e6e0,#dcdfd8 60%,#e7e3d6);border-radius:3px}

/* footer */
.site-footer{left:0;top:930px;width:870px;height:270px;background:var(--brand);color:var(--white);font-family:'Roboto',sans-serif}
.f-brand{left:76px;top:52px;display:flex;align-items:center;gap:8px;font-family:'Poppins',sans-serif;font-size:24px;font-weight:500;letter-spacing:1px}
.f-brand span.sq{width:16px;height:16px;background:var(--white)}
.f-about{left:64px;top:155px;width:178px;text-align:center;font-size:9.3px;line-height:14px}
.f-col h4{font-size:11.4px;font-weight:500;letter-spacing:.2px;margin-bottom:8px}
.f-col li{list-style:none;font-size:10.3px;line-height:18px;padding-left:3px}
.f-contact p{display:flex;gap:6px;font-size:9.5px;line-height:14px;margin-bottom:4px}
.social{left:613px;top:170px;display:flex;gap:10px}
.social i{width:8px;height:8px;background:var(--white);border-radius:50%;display:block}
.f-rule{left:64px;top:229px;width:742px;height:1px;background:var(--rule)}
.copy{left:64px;top:244px;font-size:9.6px;font-weight:500}
.legal{right:64px;top:244px;font-size:9.6px;font-weight:500}
.to-top{left:825px;top:1147px;width:25px;height:25px;border-radius:50%;background:var(--white);display:flex;align-items:center;justify-content:center}
</style>
</head>
<body>

<header class="site-header abs">
  <div class="brand abs"><span class="brand-mark"></span>FERNBOLT</div>
  <nav class="main-nav abs"><span>Today's Deals</span><span>Help</span><span>Registry</span><span>Gift Cards</span><span>Sell</span></nav>
  <div class="top-links abs">One Request, Multiple Quotes &nbsp;| &nbsp;Shop Today's Deals</div>
  <div class="search abs">
    <div class="cat">ALL</div>
    <div class="ph">Search for Products, Brands and More</div>
    <div class="go"><svg width="11" height="11" viewBox="0 0 12 12"><circle cx="5" cy="5" r="3.8" fill="none" stroke="#fff" stroke-width="1.4"/><path d="M8 8l3 3" stroke="#fff" stroke-width="1.4"/></svg></div>
  </div>
  <div class="acct abs" style="left:570px">
    <svg width="18" height="20" viewBox="0 0 18 20"><circle cx="9" cy="6" r="4.5" fill="none" stroke="#fff" stroke-width="1.4"/><path d="M1 19c0-5 4-7 8-7s8 2 8 7" fill="none" stroke="#fff" stroke-width="1.4"/></svg>
    <div>Sign In Join Free<br><b>Fernbolt</b></div>
  </div>
  <div class="acct abs" style="left:669px">
    <svg width="17" height="21" viewBox="0 0 17 21"><rect x="1" y="6" width="15" height="14" fill="none" stroke="#fff" stroke-width="1.4"/><path d="M5 8V4a3.5 3.5 0 017 0v4" fill="none" stroke="#fff" stroke-width="1.4"/></svg>
    <div>Order<br>Protection</div>
  </div>
  <div class="acct abs" style="left:739px">
    <svg width="22" height="20" viewBox="0 0 22 20"><path d="M11 19L2.5 10.5a5 5 0 017.5-7L11 4.5l1-1a5 5 0 017.5 7z" fill="none" stroke="#fff" stroke-width="1.4"/></svg>
    <div>0<br>Favorites</div>
  </div>
</header>

<div class="title-bar abs">
  <h1>CONTACT US</h1>
  <div class="crumbs">Home / Contact Us</div>
</div>

<main>
  <h2 class="section-title abs" style="left:63px">LEAVE US A MESSAGE</h2>
  <p class="lead abs" style="left:64px">There are many variations of passages of Lorem Ipsum available, but the majority Lorem Ipsum available.</p>
  <div class="field abs" style="left:64px;top:278px;width:180px;height:29px">Name</div>
  <div class="field abs" style="left:250px;top:278px;width:180px;height:29px">Email</div>
  <div class="field abs" style="left:64px;top:312px;width:366px;height:30px">Subject</div>
  <div class="field abs" style="left:64px;top:349px;width:366px;height:103px">Message</div>
  <div class="send abs">SEND</div>

  <h2 class="section-title abs" style="left:459px">CONTACT ADDRESS</h2>
  <p class="lead abs" style="left:460px;width:330px">There are many variations of passages of Lorem Ipsum available, but the majority Lorem Ipsum available.</p>
  <h3 class="info-h abs" style="top:281px">Our Address</h3>
  <p class="info-t abs" style="top:301px">House. 9, Road. 12, Widgets. Orled. Sydney. 123.</p>
  <h3 class="info-h abs" style="top:329px">Phone Number</h3>
  <p class="info-t abs" style="top:350px">01234 567 890<br>01234 567 891</p>
  <h3 class="info-h abs" style="top:397px">Web Address</h3>
  <p class="info-t abs" style="top:419px">info@example.com<br>www.example.com</p>

  <div class="map abs" role="img" aria-label="Street map showing the office location">
    <svg class="abs" style="left:461px;top:143px" width="22" height="28" viewBox="0 0 22 28"><path d="M11 27C4 18 1 14 1 10a10 10 0 0120 0c0 4-3 8-10 17z" fill="#3f5e8c"/><circle cx="11" cy="10" r="3.5" fill="#fff"/></svg>
  </div>
</main>

<footer class="site-footer abs">
  <div class="f-brand abs"><span class="sq"></span>FERNBOLT</div>
  <p class="f-about abs">Lorem ipsum dolor sit amet, consectetur adipisicing elit, sed do eiusmod .</p>
  <div class="f-col abs" style="left:297px;top:65px"><h4>INFORMATION</h4><ul><li>My Account</li><li>Wishlist</li><li>About Us</li><li>Contact Us</li><li>Blog</li></ul></div>
  <div class="f-col abs" style="left:450px;top:65px"><h4>QUICK LINKS</h4><ul><li>Shipping policy</li><li>Size Chart</li><li>Login</li><li>My Account</li><li>Register</li></ul></div>
  <div class="f-col f-contact abs" style="left:613px;top:65px;width:195px">
    <h4>CONTACT US</h4>
    <p><svg width="8" height="10" viewBox="0 0 8 10"><path d="M4 10C1 6 0 5 0 4a4 4 0 018 0c0 1-1 2-4 6z" fill="#fff"/></svg><span>Your current address goes to here,120 example, country.</span></p>
    <p><svg width="9" height="9" viewBox="0 0 9 9"><path d="M2 0l2 2-1 1.5c.6 1.2 1.3 1.9 2.5 2.5L7 5l2 2-1.5 2C3.5 9 0 5.5 0 1.5z" fill="#fff"/></svg><span>(008) 254 254 254 25487</span></p>
    <p><svg width="9" height="8" viewBox="0 0 9 8"><rect width="9" height="8" fill="#fff"/><path d="M0 0l4.5 4L9 0" fill="none" stroke="#3f5e8c"/></svg><span>example@admin.com</span></p>
  </div>
  <div class="social abs"><i></i><i></i><i></i><i></i><i></i><i></i></div>
  <div class="f-rule abs"></div>
  <div class="copy abs">© 2020 Fernbolt | All Rights Reserved.</div>
  <div class="legal abs">PRIVACY POLICY - TERMS OF USE</div>
</footer>
<div class="to-top abs"><svg width="8" height="6" viewBox="0 0 8 6"><path d="M1 5l3-3 3 3" fill="none" stroke="#3f5e8c" stroke-width="1.5"/></svg></div>

</body>
</html>
```